New Corporate Business Card - Velmorana

What we need:
We need a new corporate business card.
We want a new template that we can change by ourself.
We want business card modern and minimalist but that looks professional.
We will print it in 300 gr soft-touch.
Why not a white side with the logo and a red/grey side with the content?
Why not a grey side and a red side like our logo?
I am sure that you have better idea than ours that's the reason we come here.

Who we are:
We are a private label company in cosmetics based in Switzerland. We work in BtoB. We make skin care products for other brands.

Target Market(s)

B to B - Worldwide - any gender

Industry/Entity Type

Cosmetics

Contact Information for Business Card

Side 1:
Logo
Your Swiss Private Label Manufacturer or www.velmorana-example.ch

Side 2:
Name and surname (Example: Lucien Marchetaz)
Job Description (General Manager)
Telephone (+41 32 915 63 00)
Direct (+41 32 915 63 63)
Email (lucien.marchetaz@velmorana-example.ch)
Chemin des Pélerines 14, 2000 Neuchâtel, Switzerland
www.velmorana-example.ch

Font styles to use
Serif
Sans Serif

Requirements
Must have
• You can use 4 colors: white, red, grey and/or black .
Should not have
• Too much colors, too much things. We want it simple!

```html
<!DOCTYPE html>
<html lang="en">
<head>
<meta charset="utf-8">
<title>Velmorana – Business Card</title>
<link rel="stylesheet" href="https://fonts.googleapis.com/css2?family=Open+Sans:wght@400;700&display=swap">
<style>
  :root {
    --red: #e42d3a;
    --grey: #aeaeae;
    --grey-text: #9a9a9a;
    --dark: #2b2b2b;
    --rule: #c9c9c9;
    --white: #ffffff;
    --stage: #e6e6e6;
  }
  * { box-sizing: border-box; margin: 0; padding: 0; }
  html, body { width: 1200px; height: 856px; overflow: hidden; }
  body {
    background: var(--stage);
    font-family: "Open Sans", Arial, sans-serif;
    position: relative;
  }
  .card {
    position: absolute;
    top: 256px;
    width: 540px;
    height: 344px;
    border-radius: 26px;
    overflow: hidden;
    background: var(--white);
    box-shadow: 0 6px 18px rgba(0,0,0,.12);
  }

  /* Side 1 – brand side */
  .card--brand { left: 630px; padding: 8px; }
  .brand-face {
    width: 100%; height: 100%;
    border-radius: 20px;
    overflow: hidden;
    display: flex; flex-direction: column;
  }
  .brand-band {
    flex: 0 0 46%;
    background: var(--red);
    display: flex; align-items: center; justify-content: center;
    gap: 14px;
    padding-top: 20px;
  }
  .brand-band .square { width: 18px; height: 18px; background: var(--white); }
  .brand-name {
    font-weight: 700;
    font-size: 44px;
    color: var(--white);
  }
  .brand-rest {
    flex: 1;
    background: var(--grey);
    display: flex; align-items: center; justify-content: center;
  }
  .brand-url {
    font-size: 18px;
    color: var(--white);
  }

  /* Side 2 – contact side */
  .card--contact { left: 30px; }
  .identity {
    position: absolute; left: 34px; top: 104px; width: 200px;
  }
  .identity-mark {
    display: flex; align-items: center; gap: 10px;
    margin-bottom: 18px;
  }
  .identity-mark .square { width: 14px; height: 14px; background: var(--red); }
  .identity-mark .name {
    font-weight: 700; font-size: 26px;
    color: var(--red);
  }
  .person-name { font-size: 15px; color: var(--red); font-weight: 700; }
  .person-role { font-size: 13px; color: var(--grey-text); margin-top: 2px; }
  .divider {
    position: absolute; left: 242px; top: 78px;
    width: 1.5px; height: 146px; background: var(--rule);
  }
  .contact-list {
    position: absolute; left: 260px; top: 86px;
    list-style: none;
    font-size: 11px; color: var(--dark);
    display: flex; flex-direction: column; gap: 9px;
    white-space: nowrap;
  }
  .contact-list li { display: flex; align-items: flex-start; gap: 8px; line-height: 1.45; }
  .contact-list svg { flex: 0 0 14px; width: 14px; height: 14px; margin-top: 1px; }
  .contact-list .address { color: var(--red); font-weight: 700; }
  .stripe {
    position: absolute; left: 0; bottom: 30px; height: 5px; width: 100%;
    display: flex;
  }
  .stripe .red { flex: 1; background: var(--red); }
  .stripe .grey { flex: 0 0 110px; background: #555; }
</style>
</head>
<body>

<section class="card card--contact" aria-label="Business card, contact side">
  <div class="identity">
    <div class="identity-mark">
      <span class="square"></span>
      <span class="name">Velmorana</span>
    </div>
    <p class="person-name">Lucien Marchetaz</p>
    <p class="person-role">General Manager</p>
  </div>
  <div class="divider"></div>
  <ul class="contact-list">
    <li>
      <svg viewBox="0 0 14 14" aria-hidden="true"><circle cx="7" cy="7" r="7" fill="var(--red)"/><path d="M7 3.2a2.4 2.4 0 0 0-2.4 2.4c0 1.8 2.4 4.9 2.4 4.9s2.4-3.1 2.4-4.9A2.4 2.4 0 0 0 7 3.2z" fill="#fff"/><circle cx="7" cy="5.6" r="0.9" fill="var(--red)"/></svg>
      <span class="address">Chemin des Pélerines 14,<br>2000 Neuchâtel, Switzerland</span>
    </li>
    <li>
      <svg viewBox="0 0 14 14" aria-hidden="true"><circle cx="7" cy="7" r="7" fill="var(--red)"/><path d="M3.6 5.2c0-1 1.5-1.6 3.4-1.6s3.4.6 3.4 1.6v.6H8.6v-.8H5.4v.8H3.6zM4.6 6.4h4.8l.8 3.6H3.8z" fill="#fff"/></svg>
      <span>+41 32 915 63 00</span>
    </li>
    <li>
      <svg viewBox="0 0 14 14" aria-hidden="true"><circle cx="7" cy="7" r="7" fill="var(--red)"/><path d="M3.6 5.2c0-1 1.5-1.6 3.4-1.6s3.4.6 3.4 1.6v.6H8.6v-.8H5.4v.8H3.6zM4.6 6.4h4.8l.8 3.6H3.8z" fill="#fff"/></svg>
      <span>+41 32 915 63 63</span>
    </li>
    <li>
      <svg viewBox="0 0 14 14" aria-hidden="true"><circle cx="7" cy="7" r="7" fill="var(--red)"/><rect x="3.5" y="4.6" width="7" height="4.8" fill="#fff"/><path d="M3.5 4.6L7 7.4l3.5-2.8" fill="none" stroke="var(--red)" stroke-width="0.8"/></svg>
      <span>lucien.marchetaz@velmorana-example.ch</span>
    </li>
  </ul>
  <div class="stripe"><span class="red"></span><span class="grey"></span></div>
</section>

<section class="card card--brand" aria-label="Business card, brand side">
  <div class="brand-face">
    <div class="brand-band">
      <span class="square"></span>
      <span class="brand-name">Velmorana</span>
    </div>
    <div class="brand-rest">
      <span class="brand-url">www.velmorana-example.ch</span>
    </div>
  </div>
</section>

</body>
</html>
```